Brisko Sky Park needs a new upscale business card design for our high end aircraft hangar complex

Brisko Sky Park (BSP) is a large, upscale jet hangar complex in the US housing expensive aircraft. We need a new business card design, using our current logo. We will be attending a industry convention and need a card design that will stand out and be remembered by aircraft owners and private pilots.

Target Market(s)

Aircraft pilots or owners looking for a new upscale hangar

Industry/Entity Type

Airport

Contact Information for Business Card

I like to use very heavy card stock, 400#, double sided. Square, no rounded edges please.

Colors
3276b5
0255a3
85abd2

Requirements
Must have
• An expensive, classy design, vivid colors.
Nice to have
• Needs to look very expensive and classy, and have some "pop". Designer must be able to download or copy my current typeface or fonts.
• One card side might be black with the "Logo and Brisko Sky Park Double line image in blue (or try gold, or glossy black), and perhaps have a grayed out "K480 jet silhouette". The other card side would have our contact info, and perhaps the "BSP Logo only". I'd like my contact info 'stacked', not in a paragraph format.
Should not have
• Should not look "too busy". Having a double-sided card will help.

```html
<!DOCTYPE html>
<html lang="en">
<head>
<meta charset="utf-8">
<title>Brisko Sky Park – Business Card</title>
<link href="https://fonts.googleapis.com/css2?family=Arimo:wght@400;700&display=swap" rel="stylesheet">
<style>
  :root {
    --stage: #e9e9ec;
    --card: #1d1e21;
    --brand-blue: #3276b5;
    --brand-deep: #0255a3;
    --brand-light: #85abd2;
    --ink: #f2f2f2;
    --rule: #d8d8d8;
  }
  * { margin: 0; padding: 0; box-sizing: border-box; }
  html, body { width: 1200px; height: 787px; overflow: hidden; }
  body {
    background: var(--stage);
    font-family: "Arimo", Arial, sans-serif;
    position: relative;
  }
  .card {
    position: absolute;
    width: 520px;
    height: 297px;
    background: var(--card);
    box-shadow: 0 6px 18px rgba(0,0,0,.25);
    top: 245px;
  }
  .card--front { left: 50px; }
  .card--back { left: 630px; }

  /* front */
  .front-mark {
    position: absolute;
    left: 0; right: 0; top: 92px;
    display: flex; justify-content: center; align-items: center; gap: 14px;
  }
  .front-mark .mark-square { width: 22px; height: 22px; background: var(--brand-blue); }
  .front-mark .mark-name {
    font-weight: 700; font-size: 70px; color: var(--brand-blue); letter-spacing: 4px; line-height: 1;
  }
  .front-web {
    position: absolute; left: 0; right: 0; bottom: 48px;
    text-align: center; color: var(--ink); font-size: 13px; letter-spacing: 4px;
  }

  /* back */
  .person { position: absolute; left: 28px; top: 62px; }
  .person-name { color: var(--brand-blue); font-size: 19px; font-weight: 400; }
  .person-title { color: var(--ink); font-size: 13px; margin-top: 3px; }
  .rule { position: absolute; height: 1px; background: var(--rule); }
  .rule--top { left: 24px; top: 112px; width: 270px; }
  .rule--bottom { left: 300px; top: 214px; width: 196px; }
  .contact-list { position: absolute; left: 28px; top: 122px; list-style: none; }
  .contact-list li {
    display: flex; align-items: center; gap: 10px;
    color: var(--ink); font-size: 12.5px; height: 20px;
  }
  .contact-list svg { width: 13px; height: 13px; fill: var(--brand-blue); flex: none; }
  .back-mark {
    position: absolute; right: 28px; top: 86px; width: 170px; text-align: center;
  }
  .back-mark .mark-name {
    font-weight: 700; color: var(--brand-blue); font-size: 50px; letter-spacing: 4px; line-height: 1;
  }
  .back-mark .mark-full {
    font-weight: 700; color: var(--brand-blue); font-size: 15px; letter-spacing: 2px; margin-top: 6px;
  }
  .address {
    position: absolute; right: 28px; top: 226px; text-align: right;
    color: var(--ink); font-size: 13px; line-height: 19px;
  }
  .address .web { letter-spacing: 3px; }
</style>
</head>
<body>
  <section class="card card--front" aria-label="Card front">
    <div class="front-mark">
      <span class="mark-square"></span>
      <span class="mark-name">BSP</span>
    </div>
    <p class="front-web">www.briskosky.com</p>
  </section>

  <section class="card card--back" aria-label="Card back">
    <div class="person">
      <p class="person-name">Evan Marlo</p>
      <p class="person-title">President</p>
    </div>
    <div class="rule rule--top"></div>
    <ul class="contact-list">
      <li><svg viewBox="0 0 16 16" aria-hidden="true"><path d="M3 1h3l1.5 4-2 1.2a8 8 0 0 0 4.3 4.3L11 8.5l4 1.5v3a2 2 0 0 1-2 2A12 12 0 0 1 1 3a2 2 0 0 1 2-2z"/></svg>555 0142 7718</li>
      <li><svg viewBox="0 0 16 16" aria-hidden="true"><path d="M4.5 0h7A1.5 1.5 0 0 1 13 1.5v13a1.5 1.5 0 0 1-1.5 1.5h-7A1.5 1.5 0 0 1 3 14.5v-13A1.5 1.5 0 0 1 4.5 0zM5 2v10h6V2zm3 11a1 1 0 1 0 0 2 1 1 0 0 0 0-2z"/></svg>555 0187 2094</li>
      <li><svg viewBox="0 0 16 16" aria-hidden="true"><path d="M4 1h6l2 2v3H4zM2 7h12a1 1 0 0 1 1 1v6H1V8a1 1 0 0 1 1-1zm2 3v2h8v-2z"/></svg>555 0163 4471</li>
      <li><svg viewBox="0 0 16 16" aria-hidden="true"><path d="M1 3h14v1.2L8 9 1 4.2zm0 2.6 7 4.8 7-4.8V13H1z"/></svg>evan@briskosky.com</li>
    </ul>
    <div class="back-mark">
      <p class="mark-name">BSP</p>
      <p class="mark-full">BRISKO SKY PARK</p>
    </div>
    <div class="rule rule--bottom"></div>
    <div class="address">
      <p>1270 Harrow Lane</p>
      <p>Cedar Ridge, NY 12040</p>
      <p class="web">www.briskosky.com</p>
    </div>
  </section>
</body>
</html>
```